Redesign screen for Savings Mobile App

We need a resign of our whole app. This time, we are offering the redesign of one of the screens to see all your potential. Our intention later is to do the whole app, plus corporate web site, brochures, business cards, etc. So yes there is more to work on in the near future.
Let me share some details about what the app does and is it about:
-Focused on customer fidelity to small and medium businesses.
-The app lets the customers win free samples, discounts, gifts on the store that they like. Money savings basically.
-It will be mostly used by young users (female and male) around 18 to 40 years old.
-The app focus on get free discounts, gifts as free coffees, ice-creams, etc.
-Will use a lot of pinwharf in terms of announcements, sharing and more.

So the design should look fresh and funny. This is an hybrid html5/css3 android app. Our focus is now Android so please make sure to follow http://www.zorvelo.com/design/

The attached screenshot is a sample of the working app that we have now. Notice that it lacks of design, it is basically just a raw design of the controls that we needed in place. That is why we need your creativity.

Here we are looking for basically 2 new redesigns:
1 - The screen per se.
2 - The fortune wheel. I attached a screenshot of one that I like. Of course it should not be the same but follow the same idea.

Industry/Entity Type

Store

Font styles to use
Other font styles liked:
• Signika

Requirements
Must have
• Fresh and Funny design
Should not have
• Dark and negative colors

```html
<!DOCTYPE html>
<html lang="es">
<head>
<meta charset="utf-8">
<title>A Jugar – Ruleta de premios</title>
<link rel="stylesheet" href="https://fonts.googleapis.com/css2?family=Roboto:wght@400;500&display=swap">
<style>
  :root {
    --stage-light: #4a9fd8;
    --stage-dark: #2466a0;
    --bar-black: #0b0b0b;
    --screen-dark: #141f22;
    --accent-blue: #1a9fd9;
    --accent-blue-deep: #1383b8;
    --mint: #3fd6b4;
    --text-light: #e8eef0;
    --wheel-face: #f2f5f7;
    --wheel-line: #d3dbe0;
    --icon-blue: #3b8fc4;
    --logo-green: #1f6b4e;
  }
  * { box-sizing: border-box; margin: 0; padding: 0; }
  html, body { width: 1200px; height: 900px; overflow: hidden; }
  body {
    background: radial-gradient(ellipse at center, var(--stage-light) 0%, var(--stage-dark) 100%);
    font-family: "Roboto", Arial, sans-serif;
    display: flex; align-items: center; justify-content: center;
  }
  .app-screen {
    width: 440px; height: 820px;
    background: var(--screen-dark);
    display: flex; flex-direction: column;
    box-shadow: 0 20px 50px rgba(0,0,0,.35);
  }
  .status-bar {
    height: 28px; background: var(--bar-black);
    display: flex; align-items: center; justify-content: flex-end;
    gap: 8px; padding: 0 12px; color: #fff; font-size: 14px;
  }
  .action-bar {
    height: 60px; background: var(--accent-blue);
    display: flex; align-items: center; justify-content: center;
    color: #fff; font-size: 21px;
  }
  .content { flex: 1; padding: 30px 30px 0; display: flex; flex-direction: column; align-items: center; }
  .welcome { font-size: 25px; color: var(--accent-blue); align-self: flex-start; }
  .welcome .store { color: var(--mint); }
  .store-mark { display: flex; align-items: center; gap: 10px; margin: 22px 0 20px; }
  .store-mark .dot { width: 46px; height: 46px; border-radius: 50%; background: var(--logo-green); }
  .store-mark .name { color: var(--text-light); font-size: 16px; }
  .intro { color: var(--text-light); font-size: 16px; line-height: 1.45; text-align: center; margin-bottom: 28px; }
  .prize-wheel { width: 270px; height: 270px; }
  .spin-button {
    height: 66px; margin: 0 22px 26px; background: var(--accent-blue);
    color: #fff; font-size: 21px; display: flex; align-items: center; justify-content: center;
  }
  .nav-bar {
    height: 64px; background: var(--bar-black);
    display: flex; align-items: center; justify-content: space-around; padding: 0 40px;
  }
</style>
</head>
<body>
  <main class="app-screen">
    <div class="status-bar">
      <svg width="16" height="14" viewBox="0 0 16 14"><path d="M8 13 0 4a12 12 0 0 1 16 0z" fill="#fff"/></svg>
      <svg width="14" height="14" viewBox="0 0 14 14"><path d="M0 14 14 0v14z" fill="#fff"/></svg>
      <svg width="8" height="14" viewBox="0 0 8 14"><rect x="0" y="2" width="8" height="12" fill="#fff"/><rect x="2" y="0" width="4" height="2" fill="#fff"/></svg>
      <span class="clock">12:30</span>
    </div>
    <header class="action-bar">A Jugar !!!</header>

    <section class="content">
      <h1 class="welcome">Bienvenido a <span class="store">Cafe Loriente</span></h1>
      <div class="store-mark"><span class="dot"></span><span class="name">Cafe Loriente</span></div>
      <p class="intro">Hacé girar la ruleta y ganate desde ricos capuchinos, tostados, tortas y mucho mas...</p>

      <svg class="prize-wheel" viewBox="0 0 200 200" aria-label="Ruleta de premios">
        <circle cx="100" cy="100" r="98" fill="var(--wheel-face)"/>
        <g stroke="var(--wheel-line)" stroke-width="1.5">
          <line x1="100" y1="2" x2="100" y2="198"/>
          <line x1="2" y1="100" x2="198" y2="100"/>
          <line x1="31" y1="31" x2="169" y2="169"/>
          <line x1="169" y1="31" x2="31" y2="169"/>
        </g>
        <g fill="var(--icon-blue)">
          <rect x="128" y="36" width="22" height="14" rx="2"/>
          <circle cx="170" cy="112" r="7"/>
          <rect x="128" y="152" width="22" height="14" rx="2"/>
          <circle cx="88" cy="172" r="7"/>
          <rect x="36" y="126" width="22" height="14" rx="2"/>
          <circle cx="30" cy="88" r="7"/>
          <rect x="50" y="40" width="22" height="14" rx="2"/>
          <circle cx="112" cy="28" r="7"/>
        </g>
        <circle cx="100" cy="100" r="34" fill="var(--accent-blue-deep)"/>
        <circle cx="100" cy="100" r="27" fill="var(--accent-blue)"/>
        <path d="M94 68 100 52 106 68z" fill="#1b2428"/>
      </svg>
    </section>

    <div class="spin-button">Girar la ruleta ahora !!!</div>

    <nav class="nav-bar">
      <svg width="34" height="20" viewBox="0 0 34 20"><path d="M10 2 2 9l8 7M2 9h20a8 5 0 0 1 0 10h-4" fill="none" stroke="#ddd" stroke-width="2.5"/></svg>
      <svg width="34" height="20" viewBox="0 0 34 20"><path d="M4 18 17 3l13 15" fill="none" stroke="#ddd" stroke-width="2.5"/></svg>
      <svg width="34" height="22" viewBox="0 0 34 22"><rect x="9" y="7" width="22" height="13" fill="none" stroke="#ddd" stroke-width="2.5"/><path d="M4 15V2h22" fill="none" stroke="#ddd" stroke-width="2.5"/></svg>
    </nav>
  </main>
</body>
</html>
```